Colin Marsh Optometry "we are moving" - to be used as a business card size magnet

Our optometry business "Colin Marsh Optometry" is moving location at the end of 2017. We plan to have business card size magnets printed to hand to our current customers to remind them that we are moving at the end of this year. We would like a clean, simple design that uses our logo and colour branding (see uploaded business card) with our new address "42 Wattle Lane Muswellbrook" our phone number "6732 1804" and "same great people, same great service" and "just next to the Silver Crest Dentist".

```html
<!DOCTYPE html>
<html lang="en">
<head>
<meta charset="utf-8">
<title>Colin Marsh Optometry – We Are Moving Magnet</title>
<link rel="stylesheet" href="https://fonts.googleapis.com/css2?family=Arimo:wght@400;700&display=swap">
<style>
  :root {
    --plum: #4f3a5a;
    --plum-soft: #6e5a78;
    --ink: #2a2430;
    --card: #ffffff;
    --backdrop: #a79d95;
  }
  html, body {
    margin: 0;
    width: 1200px;
    height: 1072px;
    overflow: hidden;
    background: var(--backdrop);
    font-family: "Arimo", Arial, sans-serif;
  }
  .card {
    position: absolute;
    left: 150px;
    top: 261px;
    width: 900px;
    height: 550px;
    background: var(--card);
    overflow: hidden;
    box-shadow: 0 6px 24px rgba(0,0,0,0.18);
  }
  .card__band {
    position: absolute;
    inset: 0;
  }
  .brand {
    position: absolute;
    left: 60px;
    top: 40px;
    display: flex;
    align-items: center;
    gap: 16px;
    color: var(--plum);
  }
  .brand__dot {
    width: 16px;
    height: 16px;
    border-radius: 50%;
    background: var(--plum);
  }
  .brand__first {
    display: block;
    font-size: 24px;
    line-height: 26px;
  }
  .brand__second {
    display: block;
    font-size: 38px;
    line-height: 40px;
    font-weight: 700;
  }
  .moving {
    position: absolute;
    left: 60px;
    top: 140px;
    color: var(--plum);
  }
  .moving__title {
    margin: 0;
    font-size: 46px;
    line-height: 52px;
    font-weight: 700;
  }
  .moving__when {
    margin: 2px 0 0;
    font-size: 22px;
    line-height: 28px;
    color: var(--ink);
  }
  .moving__slogan {
    margin: 14px 0 0;
    font-size: 22px;
    line-height: 28px;
    font-weight: 700;
    color: var(--plum-soft);
  }
  .contacts {
    position: absolute;
    left: 60px;
    top: 318px;
    margin: 0;
    padding: 0;
    list-style: none;
    color: var(--ink);
    font-size: 22px;
    line-height: 36px;
  }
  .contacts li {
    display: flex;
    align-items: center;
    gap: 14px;
  }
  .contacts svg {
    width: 20px;
    height: 20px;
    fill: var(--plum);
    flex: none;
  }
  .contacts__note {
    font-size: 18px;
    color: var(--plum-soft);
  }
  .person {
    position: absolute;
    right: 56px;
    bottom: 56px;
    text-align: right;
    color: #fff;
    font-size: 18px;
    line-height: 26px;
  }
  .person__name {
    font-size: 30px;
    font-weight: 700;
    line-height: 38px;
  }
</style>
</head>
<body>
  <div class="card">
    <svg class="card__band" viewBox="0 0 900 550" aria-hidden="true">
      <defs>
        <linearGradient id="bandSheen" x1="0" y1="0" x2="1" y2="1">
          <stop offset="0" stop-color="#4a3555"/>
          <stop offset="0.45" stop-color="#7a6884"/>
          <stop offset="1" stop-color="#4f3a5a"/>
        </linearGradient>
      </defs>
      <path d="M380 550 Q600 270 900 40 L900 550 Z" fill="url(#bandSheen)"/>
      <path d="M420 550 Q630 285 900 78" fill="none" stroke="#fff" stroke-width="7"/>
    </svg>

    <div class="brand">
      <span class="brand__dot"></span>
      <span class="brand__name">
        <span class="brand__first">Colin Marsh</span>
        <span class="brand__second">Optometry</span>
      </span>
    </div>

    <div class="moving">
      <h1 class="moving__title">We are moving</h1>
      <p class="moving__when">at the end of 2017</p>
      <p class="moving__slogan">Same great people, same great service</p>
    </div>

    <ul class="contacts">
      <li><svg viewBox="0 0 24 24"><path d="M12 2a7 7 0 0 0-7 7c0 5 7 13 7 13s7-8 7-13a7 7 0 0 0-7-7zm0 9.5A2.5 2.5 0 1 1 12 6.5a2.5 2.5 0 0 1 0 5z"/></svg>42 Wattle Lane Muswellbrook</li>
      <li class="contacts__note"><svg viewBox="0 0 24 24"><path d="M4 11h12.2l-4.6-4.6L13 5l7 7-7 7-1.4-1.4 4.6-4.6H4z"/></svg>Just next to the Silver Crest Dentist</li>
      <li><svg viewBox="0 0 24 24"><path d="M6.6 10.8a15 15 0 0 0 6.6 6.6l2.2-2.2c.3-.3.7-.4 1-.2 1.1.4 2.3.6 3.6.6.6 0 1 .4 1 1V20c0 .6-.4 1-1 1A17 17 0 0 1 3 4c0-.6.4-1 1-1h3.5c.6 0 1 .4 1 1 0 1.3.2 2.5.6 3.6.1.3 0 .7-.2 1z"/></svg>6732 1804</li>
    </ul>

    <div class="person">
      <div class="person__name">Colin Marsh</div>
      <div class="person__degree">B.Optom (Hons) Eastvale Uni</div>
      <div class="person__role">Optometrist</div>
    </div>
  </div>
</body>
</html>
```